A5 Flyer for Financial Services Business

I am after a re-design of our business flyer to fit in with our new branding style and logo colour scheme. Wanting something with a bit of designer flair that I could not create myself. I have included the flyer which I created which lacks style so dazzle me.

I want to use the same content.

Text for main body of flyer is

Are you a small business owner, tradie or PAVC Service Provider struggling to stay on top of your bookkeeping and compliance obligations? If so we would love to help you get back on track and take control of your business finances so that you can make informed business decisions and focus on what you do best.

We have over 20 years industry experience and, as a small business ourselves, we are able to offer our clients a personal bookkeeping solution tailored to meet the needs of your business.

Accounts Payable | Accounts Receivable
Customer Invoicing
Bank and Credit Card Reconciliations
Payroll | Superannuation | Payroll Tax
Business Activity | Instalment Activity Statements
Regular Financial Reports
Ledgerly and Bookwise Set-Up and Training

```html
<!DOCTYPE html>
<html lang="en">
<head>
<meta charset="utf-8">
<title>Even Ledger Financial Services – Bookkeeping Flyer</title>
<link href="https://fonts.googleapis.com/css2?family=Montserrat:wght@300;400;500;600;700;800&family=Poppins:wght@800&display=swap" rel="stylesheet">
<style>
  :root{
    --teal:#0e8d92;
    --teal-deep:#0a5e73;
    --teal-text:#0f6b8a;
    --ink:#2f2f2f;
    --charcoal:#444446;
    --icon:#3a3a3c;
    --panel:#f5f5f5;
    --white:#ffffff;
    --grey-photo-a:#e9e9e9;
    --grey-photo-b:#bdbdbd;
    --badge-fill:#e4e4e4;
  }
  *{box-sizing:border-box;margin:0;padding:0}
  html,body{width:686px;height:1200px;overflow:hidden;background:var(--white)}
  body{font-family:"Montserrat",Arial,sans-serif;color:var(--ink)}
  .flyer{position:relative;width:686px;height:1200px;overflow:hidden;background:var(--white)}

  .header{position:absolute;left:0;top:0;width:686px;height:180px;background:var(--white)}
  .header-photo{position:absolute;right:0;top:0;width:420px;height:180px;
    background:linear-gradient(90deg,var(--white) 0%,var(--grey-photo-a) 35%,var(--grey-photo-b) 100%)}
  .brand{position:absolute;left:50px;top:92px}
  .brand-mark{display:inline-block;width:20px;height:20px;background:var(--teal);margin-bottom:10px}
  .brand-name{font-size:25px;font-weight:300;color:var(--teal-deep);letter-spacing:-.2px;line-height:1}
  .brand-sub{font-size:13px;font-weight:300;letter-spacing:6.2px;color:#666;margin-top:4px}

  .hero{position:absolute;left:0;top:180px;width:686px;height:224px;
    background:linear-gradient(180deg,var(--teal) 0%,var(--teal-deep) 100%)}
  .hero h1{position:absolute;left:48px;top:50px;font-family:"Poppins","Montserrat",sans-serif;
    font-weight:800;font-size:43px;line-height:1.22;color:var(--white);letter-spacing:-.3px}

  .intro{position:absolute;left:48px;top:436px;width:292px}
  .intro p{font-size:11.2px;line-height:1.5;color:var(--ink)}
  .intro .lead{font-size:15.5px;font-weight:700;color:var(--teal-text);line-height:1.2}
  .intro .block{margin-top:14px;line-height:1.45}

  .portrait{position:absolute;left:46px;top:700px;width:216px;height:398px;
    background:linear-gradient(180deg,#e7e9ec 0%,#b7bfcb 55%,#2b3a5a 100%);border-radius:4px 4px 0 0}
  .badge{position:absolute;left:272px;top:740px;width:74px;text-align:center}
  .badge-shape{display:block;margin:0 auto;width:66px;height:66px;border-radius:50%;background:var(--badge-fill)}
  .badge-caption{font-size:9px;line-height:1.3;color:#555;margin-top:10px}

  .services{position:absolute;left:356px;top:404px;width:330px;height:720px;background:var(--panel);
    list-style:none;padding:22px 0 0 18px}
  .service{display:flex;align-items:center;height:97px}
  .service-icon{flex:none;width:62px;height:62px;border-radius:50%;background:var(--icon);
    box-shadow:0 0 0 4px var(--white),0 2px 6px 4px rgba(0,0,0,.08);display:flex;align-items:center;justify-content:center}
  .service-icon svg{width:32px;height:32px;fill:none;stroke:var(--white);stroke-width:1.6;stroke-linecap:round;stroke-linejoin:round}
  .service-label{margin-left:22px;font-size:14.6px;line-height:1.28;color:var(--ink);font-weight:400}

  .footer-shapes{position:absolute;left:0;top:1098px;width:686px;height:102px}
  .phone-text{position:absolute;left:88px;top:1128px;font-size:34px;font-weight:700;color:var(--white);letter-spacing:.3px;white-space:nowrap}
  .phone-icon{position:absolute;left:42px;top:1133px;width:32px;height:32px}
  .web-text{position:absolute;left:412px;top:1153px;font-size:12.6px;font-weight:600;color:var(--white);white-space:nowrap}
  .web-icon{position:absolute;left:388px;top:1151px;width:18px;height:18px}
</style>
</head>
<body>
<main class="flyer">

  <header class="header">
    <div class="header-photo" role="img" aria-label="Greyscale photo of a smiling businesswoman in a team meeting, fading to white"></div>
    <div class="brand">
      <span class="brand-mark"></span>
      <div class="brand-name">EVEN LEDGER</div>
      <div class="brand-sub">Financial Services</div>
    </div>
  </header>

  <section class="hero">
    <h1>Bookkeeping tailored<br>to your business needs</h1>
  </section>

  <section class="intro">
    <p>Are you a small business owner, tradie or PAVC Service Provider struggling to stay on top of your bookkeeping and compliance obligations? If so we would love to help you get back on track and take control of your business finances so that you can make informed business decisions and focus on what you do best.</p>
    <p class="block"><span class="lead">We have over 20 years industry experience</span> and, as a small business ourselves, we are able to offer our clients a personal bookkeeping solution tailored to meet the needs of your business.</p>
  </section>

  <div class="portrait" role="img" aria-label="Photo of a smiling bookkeeper in a navy blazer reaching out for a handshake"></div>

  <div class="badge">
    <span class="badge-shape" aria-hidden="true"></span>
    <p class="badge-caption">BAS agent<br>41872206</p>
  </div>

  <ul class="services">
    <li class="service">
      <span class="service-icon"><svg viewBox="0 0 32 32"><rect x="6" y="4" width="16" height="22" rx="2"/><path d="M10 9h8M10 13h8M10 17h4"/><circle cx="22" cy="22" r="5"/><path d="M22 19.5v5"/></svg></span>
      <span class="service-label">Accounts Payable |<br>Accounts Receivable</span>
    </li>
    <li class="service">
      <span class="service-icon"><svg viewBox="0 0 32 32"><circle cx="12" cy="11" r="4"/><circle cx="21" cy="12" r="3.5"/><path d="M4 26c0-5 4-8 8-8s8 3 8 8M18 19c4-1 10 1 10 7"/></svg></span>
      <span class="service-label">Customer Invoicing</span>
    </li>
    <li class="service">
      <span class="service-icon"><svg viewBox="0 0 32 32"><rect x="9" y="4" width="14" height="18" rx="2"/><path d="M16 8v10M13.5 10.5h4a1.5 1.5 0 0 1 0 3h-3a1.5 1.5 0 0 0 0 3h4"/><path d="M4 24l6-3 6 3 6-3 6 3"/></svg></span>
      <span class="service-label">Bank and Credit<br>Card Reconciliations</span>
    </li>
    <li class="service">
      <span class="service-icon"><svg viewBox="0 0 32 32"><circle cx="20" cy="10" r="6"/><path d="M20 7v6"/><path d="M4 22l6-4h6a2 2 0 0 1 0 4h-4M12 22l8-3 4 2-10 6H4"/></svg></span>
      <span class="service-label">Payroll | Superannuation<br>| Payroll Tax</span>
    </li>
    <li class="service">
      <span class="service-icon"><svg viewBox="0 0 32 32"><rect x="12" y="5" width="16" height="12" rx="1"/><path d="M15 14l4-4 3 2 4-4"/><circle cx="8" cy="9" r="3"/><path d="M4 26v-8h8v8M20 17v9"/></svg></span>
      <span class="service-label">Business Activity |<br>Instalment Activity<br>Statements</span>
    </li>
    <li class="service">
      <span class="service-icon"><svg viewBox="0 0 32 32"><rect x="7" y="4" width="18" height="24" rx="2"/><path d="M11 22v-4M15 22v-7M19 22v-5M11 9h10"/></svg></span>
      <span class="service-label">Regular Financial Reports</span>
    </li>
    <li class="service">
      <span class="service-icon"><svg viewBox="0 0 32 32"><rect x="12" y="5" width="16" height="12" rx="1"/><path d="M15 9h10M15 13h6M20 17v6l-3 4M20 23l3 4"/><circle cx="7" cy="10" r="3"/><path d="M4 27v-9h6l4-3"/></svg></span>
      <span class="service-label">Ledgerly and Bookwise<br>Set-Up and Training</span>
    </li>
  </ul>

  <svg class="footer-shapes" viewBox="0 0 686 102" aria-hidden="true">
    <polygon points="0,0 330,0 366,102 0,102" fill="var(--charcoal)"/>
    <polygon points="346,24 686,24 686,102 374,102" fill="var(--teal)"/>
  </svg>
  <svg class="phone-icon" viewBox="0 0 24 24" aria-hidden="true" fill="none" stroke="#fff" stroke-width="1.5" stroke-linejoin="round">
    <path d="M6 3l3 0 1.5 4-2 1.5a11 11 0 0 0 7 7l1.5-2 4 1.5v3a2 2 0 0 1-2 2A17 17 0 0 1 4 5a2 2 0 0 1 2-2z"/>
    <path d="M14 3a7 7 0 0 1 7 7M14 6.5a3.5 3.5 0 0 1 3.5 3.5"/>
  </svg>
  <div class="phone-text">0412 555 019</div>
  <svg class="web-icon" viewBox="0 0 24 24" aria-hidden="true" fill="none" stroke="#fff" stroke-width="1.6">
    <circle cx="12" cy="12" r="10"/><ellipse cx="12" cy="12" rx="4.5" ry="10"/><path d="M2 12h20M4 6.5h16M4 17.5h16"/>
  </svg>
  <div class="web-text">evenledgerfinancial.com.au</div>

</main>
</body>
</html>
```